We need visit card and a letter paper for our website. thx

We have a beauty clinic in Switzerland.
https://wolkenbachtal.ch
We need a visit card.

Requirements
Must have
• see colors on website

```html
<!DOCTYPE html>
<html lang="de">
<head>
<meta charset="utf-8">
<title>Wolkenbachtal – Visitenkarten</title>
<link href="https://fonts.googleapis.com/css2?family=Arimo:wght@400&display=swap" rel="stylesheet">
<style>
  :root {
    --backdrop: #e3e3e3;
    --paper: #ffffff;
    --charcoal: #231f20;
    --ink: #111111;
    --rose: #c8467a;
  }
  html, body {
    margin: 0;
    width: 1200px;
    height: 1200px;
    overflow: hidden;
    background: var(--backdrop);
    font-family: "Arimo", Arial, sans-serif;
  }
  .sheet { position: relative; width: 1200px; height: 1200px; }
  .card {
    position: absolute;
    width: 577px;
    height: 332px;
    background: var(--paper);
    box-shadow: 0 3px 6px rgba(0,0,0,0.28);
    overflow: hidden;
  }
  .card--dark { background: var(--charcoal); }
  .card--front-1 { left: 15px; top: 234px; }
  .card--back-1  { left: 605px; top: 234px; width: 580px; }
  .card--front-2 { left: 15px; top: 636px; }
  .card--back-2  { left: 605px; top: 635px; width: 580px; }

  .brand-name {
    position: absolute;
    font-family: "Arimo", Arial, sans-serif;
    font-weight: 400;
    white-space: nowrap;
    transform: translate(-50%, -50%);
    color: var(--ink);
  }
  .brand-name--small { left: 147px; top: 166px; font-size: 25px; }
  .brand-name--large { left: 290px; top: 166px; font-size: 38px; letter-spacing: 0.5px; }
  .card--dark .brand-name { color: var(--paper); }

  .divider {
    position: absolute;
    left: 281px;
    top: 93px;
    width: 1.5px;
    height: 145px;
    background: var(--rose);
  }
  .contact { position: absolute; left: 308px; top: 88px; width: 260px; color: var(--ink); }
  .contact__name { font-size: 18px; color: var(--rose); margin: 0; line-height: 22px; }
  .contact__role { font-size: 13.5px; margin: 2px 0 10px; line-height: 16px; }
  .contact__row {
    position: relative;
    font-size: 13.5px;
    line-height: 20px;
    padding-left: 16px;
    white-space: nowrap;
  }
  .contact__row--gap { margin-bottom: 7px; }
  .contact__icon { position: absolute; left: -3px; top: 4px; width: 13px; height: 13px; }
  .hotline-label { color: var(--rose); }
</style>
</head>
<body>
<main class="sheet">

  <section class="card card--front-1">
    <span class="brand-name brand-name--small">Wolkenbachtal</span>
    <div class="divider"></div>
    <div class="contact">
      <p class="contact__name">Dr. Lena Marbach</p>
      <p class="contact__role">FÄ für Plastische Chirurgie</p>
      <div class="contact__row contact__row--gap">
        <svg class="contact__icon" viewBox="0 0 14 14"><path d="M7 13 C3 8.5 2 6.5 2 5 A5 5 0 0 1 12 5 C12 6.5 11 8.5 7 13Z" fill="none" stroke="#c8467a" stroke-width="1.3"/><circle cx="7" cy="5" r="1.8" fill="none" stroke="#c8467a" stroke-width="1.2"/></svg>
        Bergweg 14, 7099 Talwil<br>Schweiz
      </div>
      <div class="contact__row">
        <svg class="contact__icon" viewBox="0 0 14 14"><path d="M3 1.5 L5 4.5 L4 6 C5 8 6 9 8 10 L9.5 9 L12.5 11 L11 13 C6 12.5 1.5 8 1 3Z" fill="none" stroke="#c8467a" stroke-width="1.3"/></svg>
        <span class="hotline-label">24h HOTLINE:</span> +41 (0) 800 20 30 40
      </div>
      <div class="contact__row">
        <svg class="contact__icon" viewBox="0 0 14 14"><rect x="1" y="3" width="12" height="8" fill="#c8467a"/><path d="M1 3 L7 8 L13 3" fill="none" stroke="#fff" stroke-width="1"/></svg>
        hallo@wolkenbachtal.ch
      </div>
      <div class="contact__row">
        <svg class="contact__icon" viewBox="0 0 14 14"><circle cx="7" cy="7" r="5.7" fill="none" stroke="#c8467a" stroke-width="1"/><ellipse cx="7" cy="7" rx="2.5" ry="5.7" fill="none" stroke="#c8467a" stroke-width="1"/><path d="M1.3 7 H12.7 M2.2 4 H11.8 M2.2 10 H11.8" stroke="#c8467a" stroke-width="1"/></svg>
        www.wolkenbachtal.ch
      </div>
    </div>
  </section>

  <section class="card card--dark card--back-1">
    <span class="brand-name brand-name--large">Wolkenbachtal</span>
  </section>

  <section class="card card--front-2">
    <span class="brand-name brand-name--small">Wolkenbachtal</span>
    <div class="divider"></div>
    <div class="contact">
      <p class="contact__name">Dr. Hofstätter Jonas, DESA</p>
      <p class="contact__role">FA für Anästhesist</p>
      <div class="contact__row contact__row--gap">
        <svg class="contact__icon" viewBox="0 0 14 14"><path d="M7 13 C3 8.5 2 6.5 2 5 A5 5 0 0 1 12 5 C12 6.5 11 8.5 7 13Z" fill="none" stroke="#c8467a" stroke-width="1.3"/><circle cx="7" cy="5" r="1.8" fill="none" stroke="#c8467a" stroke-width="1.2"/></svg>
        Bergweg 14, 7099 Talwil<br>Schweiz
      </div>
      <div class="contact__row">
        <svg class="contact__icon" viewBox="0 0 14 14"><path d="M3 1.5 L5 4.5 L4 6 C5 8 6 9 8 10 L9.5 9 L12.5 11 L11 13 C6 12.5 1.5 8 1 3Z" fill="none" stroke="#c8467a" stroke-width="1.3"/></svg>
        <span class="hotline-label">24h HOTLINE:</span> +41 (0) 800 20 30 40
      </div>
      <div class="contact__row">
        <svg class="contact__icon" viewBox="0 0 14 14"><rect x="1" y="3" width="12" height="8" fill="#c8467a"/><path d="M1 3 L7 8 L13 3" fill="none" stroke="#fff" stroke-width="1"/></svg>
        hallo@wolkenbachtal.ch
      </div>
      <div class="contact__row">
        <svg class="contact__icon" viewBox="0 0 14 14"><circle cx="7" cy="7" r="5.7" fill="none" stroke="#c8467a" stroke-width="1"/><ellipse cx="7" cy="7" rx="2.5" ry="5.7" fill="none" stroke="#c8467a" stroke-width="1"/><path d="M1.3 7 H12.7 M2.2 4 H11.8 M2.2 10 H11.8" stroke="#c8467a" stroke-width="1"/></svg>
        www.wolkenbachtal.ch
      </div>
    </div>
  </section>

  <section class="card card--back-2">
    <span class="brand-name brand-name--large">Wolkenbachtal</span>
  </section>

</main>
</body>
</html>
```